Spiritual Healing bussiness needs logo/business card

Simple, clean looking logo/card
For spiritual business with healing services and occult rituals

Contact Information for Business Card

Needs my name: Corwin Halley
Business name: Veyra Healing Shop
Services provided and worded in this way:

Reiki Healing
Tarot
Oils
Rituals Of Change

Can look occult like but with light energy.

Colors
0255a3
3276b5
85abd2
33a6d7
85cae6
0292cd

```html
<!DOCTYPE html>
<html lang="en">
<head>
<meta charset="utf-8">
<title>Veyra Healing Shop – Business Cards</title>
<link href="https://fonts.googleapis.com/css2?family=Arvo&family=Lato:wght@400&display=swap" rel="stylesheet">
<style>
  :root {
    --backdrop: #5b5b5b;
    --card-white: #ffffff;
    --brand-deep: #0255a3;
    --brand-mid: #3276b5;
    --brand-sky: #0292cd;
    --text-dark: #2b2b2b;
    --divider: #9a9a9a;
  }
  * { margin: 0; padding: 0; box-sizing: border-box; }
  html, body {
    width: 1200px; height: 802px; overflow: hidden;
    background: var(--backdrop);
  }
  .canvas { position: relative; width: 1200px; height: 802px; }
  .card {
    position: absolute; top: 274px; width: 443px; height: 265px;
    box-shadow: 2px 3px 6px rgba(0,0,0,0.45);
  }
  .card-front { left: 136px; background: var(--card-white); }
  .card-back { left: 624px; background: var(--brand-deep); overflow: hidden; }

  .brand-mark {
    position: absolute; left: 74px; top: 81px; width: 76px; height: 76px;
    border: 5px solid var(--brand-deep); border-radius: 50%;
  }
  .brand-name {
    position: absolute; left: 0; width: 238px; top: 163px; text-align: center;
    font-family: 'Arvo', serif; font-weight: 400; font-size: 18px; line-height: 24px;
    color: var(--brand-deep); white-space: nowrap;
  }
  .divider {
    position: absolute; left: 222px; top: 84px; width: 1px; height: 96px;
    background: var(--divider);
  }
  .person-name {
    position: absolute; left: 234px; top: 81px;
    font-family: 'Arvo', serif; font-weight: 400; font-size: 18px; line-height: 24px;
    color: var(--brand-mid); white-space: nowrap;
  }
  .contact-list { position: absolute; left: 235px; top: 129px; list-style: none; }
  .contact-item {
    display: flex; align-items: center; height: 17px;
    font-family: 'Lato', sans-serif; font-size: 13px; line-height: 17px;
    color: var(--text-dark); white-space: nowrap;
  }
  .contact-icon { width: 14px; height: 14px; margin-right: 3px; flex: none; }

  .emblem-pattern { position: absolute; inset: 0; background: var(--brand-deep); }
  .back-title {
    position: absolute; left: 0; width: 100%; top: 106px; text-align: center;
    font-family: 'Arvo', serif; font-weight: 400; font-size: 28px; line-height: 36px;
    color: var(--card-white); white-space: nowrap;
  }
  .service-list {
    position: absolute; left: 0; width: 100%; top: 155px; text-align: center;
    font-family: 'Lato', sans-serif; font-weight: 400; font-size: 13px; line-height: 18px;
    color: var(--card-white); white-space: nowrap;
  }
  .service-list .dot { font-size: 9px; margin: 0 2px; vertical-align: 1px; }
</style>
</head>
<body>
<main class="canvas">
  <section class="card card-front" aria-label="Business card front">
    <div class="brand-mark" aria-hidden="true"></div>
    <p class="brand-name">Veyra Healing Shop</p>
    <div class="divider"></div>
    <h1 class="person-name">Corwin Halley</h1>
    <ul class="contact-list">
      <li class="contact-item">
        <svg class="contact-icon" viewBox="0 0 14 14" aria-hidden="true"><circle cx="7" cy="7" r="6.3" fill="none" stroke="#0255a3" stroke-width="1.2"/><path d="M3.8 8.2h6.4v1.8H3.8zM4.5 6.2c0-1.4 5-1.4 5 0v1H4.5z" fill="#0255a3"/></svg>
        044-555 010 472
      </li>
      <li class="contact-item">
        <svg class="contact-icon" viewBox="0 0 14 14" aria-hidden="true"><circle cx="7" cy="7" r="6.3" fill="none" stroke="#0255a3" stroke-width="1.2"/><rect x="3.6" y="4.8" width="6.8" height="4.6" fill="#0255a3"/><path d="M3.6 4.8l3.4 2.6 3.4-2.6" fill="none" stroke="#fff" stroke-width="0.8"/></svg>
        info@veyrahealing.com
      </li>
      <li class="contact-item">
        <svg class="contact-icon" viewBox="0 0 14 14" aria-hidden="true"><circle cx="7" cy="7" r="6.3" fill="none" stroke="#0255a3" stroke-width="1.2"/><circle cx="7" cy="7" r="3.6" fill="#0255a3"/><path d="M5.2 5.6c1 .4 1.4 1.4.6 2.2M8 4.6c-.3 1 .8 1.2 1.6 1.6" fill="none" stroke="#fff" stroke-width="0.7"/></svg>
        www.VeyraHealingShop.com
      </li>
    </ul>
  </section>

  <section class="card card-back" aria-label="Business card back">
    <div class="emblem-pattern" role="img" aria-label="Repeating pattern of faint circular emblems on deep blue"></div>
    <h2 class="back-title">Veyra Healing Shop</h2>
    <p class="service-list">Reiki Healing <span class="dot">●</span>Tarot <span class="dot">●</span>Oils <span class="dot">●</span> Rituals Of Change</p>
  </section>
</main>
</body>
</html>
```